Thank you for shopping with us business card

We would like a thank you card for our rebranded business. We used to be "Kestrel Knacks" but are now "Kestrel Trinkets. Old thank you card and new logo will be attached for reference. New thank you card does not have to be same design as old thank you card, but please use new logo.
Mopsa URL is now kestreltrinkets.mopsa.com
Pictaloo is @Kestrel_Trinkets
Email is kestreltrinkets@mopsamail.com
Thank you!

Contact Information for Business Card

Mopsa site, email, Pictaloo

```html
<!DOCTYPE html>
<html lang="en">
<head>
<meta charset="utf-8">
<title>Kestrel Trinkets – Thank You Card</title>
<link rel="stylesheet" href="https://fonts.googleapis.com/css2?family=Inter:wght@400;500;700;800&display=swap">
<style>
  :root {
    --backdrop: #9a9a9a;
    --card: #1d1d1d;
    --card-front: #1a1a1a;
    --ink: #ffffff;
    --ink-soft: #e6e6e6;
    --mark-fill: #111111;
    --mark-edge: #2a2a2a;
    --front-name: #9c9c9c;
    --rule-front: #0c0c0c;
  }
  * { box-sizing: border-box; margin: 0; padding: 0; }
  html, body {
    width: 1200px; height: 588px; overflow: hidden;
    background: var(--backdrop);
    font-family: "Inter", sans-serif;
  }
  .canvas { position: relative; width: 1200px; height: 588px; }

  .card { position: absolute; width: 488px; height: 287px; overflow: hidden; }
  .card--front { left: 87px; top: 142px; background: var(--card-front); }
  .card--back  { left: 622px; top: 142px; background: var(--card); color: var(--ink); }

  /* front */
  .front-mark {
    position: absolute; left: 80px; top: 92px; width: 76px; height: 100px;
    background: var(--mark-fill); border: 1px solid var(--mark-edge);
  }
  .front-rule {
    position: absolute; left: 182px; top: 94px; width: 2px; height: 98px;
    background: var(--rule-front);
  }
  .front-name {
    position: absolute; left: 208px; top: 102px;
    font-weight: 500; font-size: 31px; line-height: 40px;
    text-transform: uppercase; letter-spacing: -0.5px;
    color: var(--front-name);
  }

  /* back */
  .brand-block {
    position: absolute; left: 24px; top: 75px; width: 142px;
    display: flex; flex-direction: column; align-items: center;
  }
  .brand-mark {
    width: 74px; height: 74px; border: 2px solid var(--ink);
  }
  .brand-name {
    margin-top: 20px; font-weight: 500; font-size: 13.5px;
    text-transform: uppercase; white-space: nowrap; letter-spacing: -0.1px;
  }
  .back-rule {
    position: absolute; left: 189px; top: 76px; width: 1.5px; height: 123px;
    background: var(--ink);
  }
  .message { position: absolute; left: 211px; top: 70px; width: 270px; }
  .message__title {
    font-weight: 800; font-size: 23.5px; line-height: 28px;
    text-transform: uppercase; letter-spacing: 0.2px;
  }
  .message__body {
    margin-top: 18px; font-size: 13.6px; line-height: 20.3px;
    color: var(--ink-soft); white-space: nowrap;
  }
  .contacts {
    position: absolute; left: 14px; right: 14px; top: 256px;
    display: flex; justify-content: space-between; align-items: center;
    font-size: 9.3px; color: var(--ink-soft); white-space: nowrap;
  }
  .contact { display: flex; align-items: center; gap: 3px; }
  .contact__dot {
    width: 7px; height: 7px; border-radius: 50%; background: var(--ink); flex: none;
  }
  .contact__icon { width: 10px; height: 7px; flex: none; }
</style>
</head>
<body>
<main class="canvas">

  <section class="card card--front" aria-label="Card front">
    <div class="front-mark" role="img" aria-label="Kestrel Trinkets logo mark"></div>
    <div class="front-rule"></div>
    <p class="front-name">Kestrel<br>Trinkets</p>
  </section>

  <section class="card card--back" aria-label="Card back">
    <div class="brand-block">
      <div class="brand-mark" role="img" aria-label="Kestrel Trinkets logo mark"></div>
      <p class="brand-name">Kestrel Trinkets</p>
    </div>
    <div class="back-rule"></div>
    <div class="message">
      <h1 class="message__title">Thank you for<br>your purchase</h1>
      <p class="message__body">Your Purchase Made my day and I<br>hope this package brightness yours.<br>Please come back and leave a review!</p>
    </div>
    <footer class="contacts">
      <span class="contact"><span class="contact__dot"></span><span>Mopsa kestreltrinkets.mopsa.com</span></span>
      <span class="contact"><span class="contact__dot"></span><span>Pictaloo @Kestrel_Trinkets</span></span>
      <span class="contact">
        <svg class="contact__icon" viewBox="0 0 11 8" aria-hidden="true">
          <rect x="0.5" y="0.5" width="10" height="7" fill="#ffffff"/>
          <path d="M0.5 0.8 L5.5 4.6 L10.5 0.8" fill="none" stroke="#1d1d1d" stroke-width="1"/>
        </svg>
        <span>kestreltrinkets@mopsamail.com</span>
      </span>
    </footer>
  </section>

</main>
</body>
</html>
```